Design a poster that illustrates the six central pillars of our school district's efforts with students. The attached PDF outlines the six main competencies we aim for students to possess upon graduation. Each of the 6 has 3 bullet points for the poster as well. The title is "Profile of a Drifter". Our mascot is this attached winged wheel. The overall concept is that staff take kids when they are young and develop these 6 things when they graduate. Our colors are navy, red, and white. We will make this poster in a variety of sizes in offices, classrooms, and in digital spaces as well. On the PDF - ignore the column that says "Synthesis". That has nothing to do with this poster.

The district is Corvath Falls Public Schools https://www.corvath.k12.example.us/

```html
<!DOCTYPE html>
<html lang="en">
<head>
<meta charset="utf-8">
<title>Profile of a Drifter – Competency Suggestions</title>
<link href="https://fonts.googleapis.com/css2?family=Bebas+Neue&family=Exo+2:wght@500;700;800&display=swap" rel="stylesheet">
<style>
  :root {
    --navy: #0e1140;
    --red: #a41c22;
    --white: #ffffff;
    --ink: #15173a;
    --rule: #1a1a1a;
  }
  * { box-sizing: border-box; margin: 0; padding: 0; }
  html, body { width: 950px; height: 1200px; overflow: hidden; background: var(--navy); }
  .poster {
    position: relative;
    width: 950px;
    height: 1200px;
    overflow: hidden;
    font-family: "Exo 2", sans-serif;
    color: var(--ink);
  }
  .backdrop { position: absolute; inset: 0; }
  .poster-title {
    position: absolute;
    left: 53px;
    top: 36px;
    font-family: "Bebas Neue", sans-serif;
    font-size: 76px;
    line-height: 1;
    letter-spacing: 0.5px;
    color: var(--white);
    font-weight: 400;
  }
  .district-mark {
    position: absolute;
    right: 58px;
    top: 58px;
    display: flex;
    align-items: center;
    gap: 10px;
    font-size: 22px;
    font-weight: 700;
    color: var(--white);
  }
  .district-mark .dot {
    width: 16px; height: 16px; border-radius: 50%;
    background: var(--red);
  }
  .competency-card {
    position: absolute;
    left: 57px;
    top: 129px;
    width: 836px;
    background: var(--white);
    border: 2px solid var(--rule);
    border-radius: 6px;
    overflow: hidden;
  }
  .card-heading {
    height: 54px;
    display: flex;
    align-items: center;
    justify-content: center;
    font-size: 27px;
    font-weight: 800;
    color: var(--red);
    letter-spacing: 0.2px;
  }
  .competency-table { width: 100%; border-collapse: collapse; table-layout: fixed; }
  .competency-table th {
    background: var(--red);
    color: var(--white);
    height: 46px;
    font-size: 18px;
    font-weight: 700;
    letter-spacing: 0.5px;
    border-top: 2px solid var(--rule);
    border-bottom: 2px solid var(--rule);
  }
  .competency-table th.col-name { text-align: left; padding-left: 14px; width: 158px; border-right: 2px solid var(--rule); }
  .competency-table th.col-details { text-align: center; }
  .competency-table td { border-top: 2px solid var(--rule); vertical-align: middle; }
  .competency-table tr:first-child td { border-top: none; }
  .competency-table td.name {
    padding-left: 14px;
    font-size: 17.5px;
    font-weight: 500;
    border-right: 2px solid var(--rule);
  }
  .detail-list { list-style: none; padding: 0 14px 0 23px; }
  .detail-list li {
    position: relative;
    padding-left: 22px;
    font-size: 16.2px;
    font-weight: 500;
    line-height: 1.32;
    margin: 13px 0;
  }
  .detail-list li svg { position: absolute; left: 0; top: 3px; width: 15px; height: 15px; }
  .site-footer {
    position: absolute;
    left: 0; top: 1108px;
    width: 950px; height: 92px;
    background: var(--navy);
    color: var(--white);
    display: flex;
    align-items: center;
    padding-left: 56px;
    font-size: 17px;
    font-weight: 500;
  }
  .footer-item { display: flex; align-items: center; gap: 8px; }
  .footer-item svg { width: 20px; height: 20px; flex: none; }
  .footer-address { margin-right: 26px; }
  .footer-address strong { display: block; font-weight: 700; font-size: 17px; }
  .footer-contact { margin-right: 16px; font-size: 18px; }
</style>
</head>
<body>
<div class="poster">
  <svg class="backdrop" width="950" height="1200" viewBox="0 0 950 1200" aria-hidden="true">
    <rect width="950" height="1200" fill="var(--navy)"/>
    <path d="M0 440 C 300 560, 650 420, 950 350 L950 1200 L0 1200 Z" fill="var(--red)"/>
    <path d="M0 440 C 300 560, 650 420, 950 350" fill="none" stroke="var(--white)" stroke-width="10"/>
    <path d="M0 500 C 300 620, 650 480, 950 410" fill="none" stroke="var(--navy)" stroke-width="12"/>
  </svg>

  <h1 class="poster-title">PROFILE OF A DRIFTER</h1>
  <div class="district-mark"><span class="dot"></span>Corvath Falls</div>

  <section class="competency-card">
    <h2 class="card-heading">COMPETENCY SUGGESTIONS</h2>
    <table class="competency-table">
      <thead>
        <tr><th class="col-name">COMPETENCY</th><th class="col-details">DETAILS</th></tr>
      </thead>
      <tbody>
        <tr style="height:130px">
          <td class="name">Communicator</td>
          <td><ul class="detail-list">
            <li><svg viewBox="0 0 16 16"><circle cx="8" cy="8" r="8" fill="var(--navy)"/><path d="M4.5 8.2l2.3 2.3 4.7-4.8" fill="none" stroke="#fff" stroke-width="2"/></svg>Expresses ideas clearly and respectfully (written &amp; verbal).</li>
            <li><svg viewBox="0 0 16 16"><circle cx="8" cy="8" r="8" fill="var(--navy)"/><path d="M4.5 8.2l2.3 2.3 4.7-4.8" fill="none" stroke="#fff" stroke-width="2"/></svg>Listens actively and understands diverse perspectives.</li>
            <li><svg viewBox="0 0 16 16"><circle cx="8" cy="8" r="8" fill="var(--navy)"/><path d="M4.5 8.2l2.3 2.3 4.7-4.8" fill="none" stroke="#fff" stroke-width="2"/></svg>Adjusts communication to suit the audience and context.</li>
          </ul></td>
        </tr>
        <tr style="height:152px">
          <td class="name">Critical Thinker</td>
          <td><ul class="detail-list">
            <li><svg viewBox="0 0 16 16"><circle cx="8" cy="8" r="8" fill="var(--navy)"/><path d="M4.5 8.2l2.3 2.3 4.7-4.8" fill="none" stroke="#fff" stroke-width="2"/></svg>Questions, analyzes, and evaluates information from multiple sources.</li>
            <li><svg viewBox="0 0 16 16"><circle cx="8" cy="8" r="8" fill="var(--navy)"/><path d="M4.5 8.2l2.3 2.3 4.7-4.8" fill="none" stroke="#fff" stroke-width="2"/></svg>Identifies and solves complex problems creatively.</li>
            <li><svg viewBox="0 0 16 16"><circle cx="8" cy="8" r="8" fill="var(--navy)"/><path d="M4.5 8.2l2.3 2.3 4.7-4.8" fill="none" stroke="#fff" stroke-width="2"/></svg>Uses evidence and diverse perspectives to form reasoned conclusions and make informed decisions.</li>
          </ul></td>
        </tr>
        <tr style="height:133px">
          <td class="name">Responsible</td>
          <td><ul class="detail-list">
            <li><svg viewBox="0 0 16 16"><circle cx="8" cy="8" r="8" fill="var(--navy)"/><path d="M4.5 8.2l2.3 2.3 4.7-4.8" fill="none" stroke="#fff" stroke-width="2"/></svg>Takes ownership of actions, choices, and commitments.</li>
            <li><svg viewBox="0 0 16 16"><circle cx="8" cy="8" r="8" fill="var(--navy)"/><path d="M4.5 8.2l2.3 2.3 4.7-4.8" fill="none" stroke="#fff" stroke-width="2"/></svg>Manages time, resources, and self to meet expectations.</li>
            <li><svg viewBox="0 0 16 16"><circle cx="8" cy="8" r="8" fill="var(--navy)"/><path d="M4.5 8.2l2.3 2.3 4.7-4.8" fill="none" stroke="#fff" stroke-width="2"/></svg>Acts with integrity and advocates for self and others.</li>
          </ul></td>
        </tr>
        <tr style="height:157px">
          <td class="name">Adaptable</td>
          <td><ul class="detail-list">
            <li><svg viewBox="0 0 16 16"><circle cx="8" cy="8" r="8" fill="var(--navy)"/><path d="M4.5 8.2l2.3 2.3 4.7-4.8" fill="none" stroke="#fff" stroke-width="2"/></svg>Responds productively to new situations, challenges, and feedback.</li>
            <li><svg viewBox="0 0 16 16"><circle cx="8" cy="8" r="8" fill="var(--navy)"/><path d="M4.5 8.2l2.3 2.3 4.7-4.8" fill="none" stroke="#fff" stroke-width="2"/></svg>Learns from new experiences &amp; applies prior knowledge in evolving contexts.</li>
            <li><svg viewBox="0 0 16 16"><circle cx="8" cy="8" r="8" fill="var(--navy)"/><path d="M4.5 8.2l2.3 2.3 4.7-4.8" fill="none" stroke="#fff" stroke-width="2"/></svg>Adjusts behavior and approach to effectively engage with diverse groups and environments.</li>
          </ul></td>
        </tr>
        <tr style="height:132px">
          <td class="name">Collaborator</td>
          <td><ul class="detail-list">
            <li><svg viewBox="0 0 16 16"><circle cx="8" cy="8" r="8" fill="var(--navy)"/><path d="M4.5 8.2l2.3 2.3 4.7-4.8" fill="none" stroke="#fff" stroke-width="2"/></svg>Contributes effectively and cooperatively to shared goals.</li>
            <li><svg viewBox="0 0 16 16"><circle cx="8" cy="8" r="8" fill="var(--navy)"/><path d="M4.5 8.2l2.3 2.3 4.7-4.8" fill="none" stroke="#fff" stroke-width="2"/></svg>Listens actively and values diverse ideas and perspectives.</li>
            <li><svg viewBox="0 0 16 16"><circle cx="8" cy="8" r="8" fill="var(--navy)"/><path d="M4.5 8.2l2.3 2.3 4.7-4.8" fill="none" stroke="#fff" stroke-width="2"/></svg>Engages respectfully, compromising and leading when appropriate.</li>
          </ul></td>
        </tr>
        <tr style="height:154px">
          <td class="name">Compassionate</td>
          <td><ul class="detail-list">
            <li><svg viewBox="0 0 16 16"><circle cx="8" cy="8" r="8" fill="var(--navy)"/><path d="M4.5 8.2l2.3 2.3 4.7-4.8" fill="none" stroke="#fff" stroke-width="2"/></svg>Understands &amp; acknowledges others’ feelings, perspectives, &amp; experiences.</li>
            <li><svg viewBox="0 0 16 16"><circle cx="8" cy="8" r="8" fill="var(--navy)"/><path d="M4.5 8.2l2.3 2.3 4.7-4.8" fill="none" stroke="#fff" stroke-width="2"/></svg>Responds with kindness, patience, and support.</li>
            <li><svg viewBox="0 0 16 16"><circle cx="8" cy="8" r="8" fill="var(--navy)"/><path d="M4.5 8.2l2.3 2.3 4.7-4.8" fill="none" stroke="#fff" stroke-width="2"/></svg>Seeks to connect with and contribute positively to the well-being of others and the community.</li>
          </ul></td>
        </tr>
      </tbody>
    </table>
  </section>

  <footer class="site-footer">
    <div class="footer-item footer-address">
      <svg viewBox="0 0 20 20"><circle cx="10" cy="10" r="10" fill="var(--red)"/><path d="M10 4.5a3.3 3.3 0 0 0-3.3 3.3c0 2.4 3.3 5.7 3.3 5.7s3.3-3.3 3.3-5.7A3.3 3.3 0 0 0 10 4.5z" fill="#fff"/><circle cx="10" cy="7.8" r="1.2" fill="var(--red)"/><path d="M5.5 15h9" stroke="#fff" stroke-width="1.2"/></svg>
      <div><strong>CORVATH FALLS PUBLIC SCHOOLS</strong>418 Lakeview Ave. Corvath Falls, MI 49800</div>
    </div>
    <div class="footer-item footer-contact">
      <svg viewBox="0 0 20 20"><circle cx="10" cy="10" r="10" fill="var(--red)"/><path d="M7 5.2l1.6 2.4-1 1.1c.7 1.5 1.8 2.6 3.3 3.3l1.1-1 2.4 1.6-.7 1.7c-4 .1-7.6-3.5-7.5-7.5z" fill="#fff"/></svg>
      231-555-0148
    </div>
    <div class="footer-item footer-contact">
      <svg viewBox="0 0 20 20"><circle cx="10" cy="10" r="10" fill="var(--red)"/><rect x="6.5" y="4.5" width="7" height="3.5" fill="#fff"/><rect x="5" y="8.5" width="10" height="5" rx="1" fill="#fff"/><rect x="7" y="11.5" width="6" height="4" fill="#fff" stroke="var(--red)" stroke-width="0.8"/></svg>
      231-555-0163
    </div>
    <div class="footer-item footer-contact">
      <svg viewBox="0 0 20 20"><circle cx="10" cy="10" r="10" fill="var(--red)"/><g fill="none" stroke="#fff" stroke-width="1.2"><circle cx="10" cy="10" r="5.5"/><ellipse cx="10" cy="10" rx="2.4" ry="5.5"/><path d="M4.5 10h11M5.3 7.3h9.4M5.3 12.7h9.4"/></g></svg>
      corvath.k12.example.us
    </div>
  </footer>
</div>
</body>
</html>
```